Business Cards Design for the electrical wholesaler: clean bold dynamic :)

We need a business card design that would follow our latest brand guidelines. As an electrical wholesaler we want to bring a fresh look and feel into the industry. The design should be clean bold and dynamic. It should come alive with the renewed energy of our green colour. Our grey colour should keep things balanced and complement the notion of maturity and responsibility. We employ Lato as a corporate font however are not bound by this font and we’re open to interpretation here.

Target Market(s)

Electrical contractors

Industry/Entity Type

Business

Contact Information for Business Card

Logo
Name & Surname: Olena Dovbush
Job Title: Director of Marketing
Email: helen.dovbush@mailvane.example
Cell phone: XXX.XXX.XXXX
Address: 20917 - 87 Ave. Edmonton, AB, Canada. T6K 2R8
Business Phone: 780.555.0187
Website: www.qorvil.example

Font styles to use
Other font styles liked:
• Lato

Requirements
Must have
• Logo & website
Nice to have
• Brand elements - some of them you may find in the attached Brand Guidelines (e.g. three lines on the background signifying "W")

```html
<!DOCTYPE html>
<html lang="en">
<head>
<meta charset="utf-8">
<title>Qorvil – Business Cards</title>
<link rel="stylesheet" href="https://fonts.googleapis.com/css2?family=Lato:ital,wght@0,400;0,700;0,900;1,400;1,700&display=swap">
<style>
  :root {
    --green: #9cc54a;
    --green-deep: #8ab83c;
    --orange: #e0682a;
    --paper: #e4e6ea;
    --grey: #4d4e50;
    --ink: #3a3b3d;
    --rule: #7f9ad3;
    --backdrop: #efeeea;
  }
  * { margin: 0; padding: 0; box-sizing: border-box; }
  html, body { width: 1200px; height: 800px; overflow: hidden; }
  body {
    background: var(--backdrop);
    font-family: "Lato", sans-serif;
    position: relative;
  }
  .card {
    position: absolute;
    left: 300px;
    width: 600px;
    height: 343px;
    background: var(--paper);
    overflow: hidden;
    box-shadow: 0 6px 18px rgba(0,0,0,.18);
  }
  .card--front { top: 29px; }
  .card--back { top: 428px; }
  .card__shapes { position: absolute; inset: 0; }

  .brand-name {
    position: absolute;
    font-weight: 900;
    color: var(--grey);
    letter-spacing: -0.5px;
    line-height: 1;
  }
  .card--front .brand-name { right: 48px; top: 58px; font-size: 44px; }
  .card--back .brand-name { left: 0; right: 0; top: 78px; text-align: center; font-size: 66px; }

  .holder {
    position: absolute;
    left: 44px;
    top: 84px;
    color: #fff;
    text-transform: uppercase;
  }
  .holder__name { font-weight: 700; font-size: 30px; letter-spacing: .5px; }
  .holder__title { font-size: 15px; letter-spacing: .6px; margin-top: 2px; }

  .contacts {
    position: absolute;
    left: 0; right: 0; top: 226px;
    display: flex;
    justify-content: space-around;
    padding: 0 20px;
  }
  .contact { display: flex; flex-direction: column; align-items: center; gap: 10px; }
  .contact__icon { width: 50px; height: 50px; }
  .contact__text { font-size: 13px; color: var(--ink); }

  .web {
    position: absolute;
    left: 0; right: 0; top: 214px;
    text-align: center;
    color: var(--ink);
  }
  .web__url { font-weight: 700; font-style: italic; font-size: 30px; letter-spacing: 4px; }
  .web__address { font-style: italic; font-size: 17px; margin-top: 12px; }
</style>
</head>
<body>

<section class="card card--front" aria-label="Business card front">
  <svg class="card__shapes" viewBox="0 0 600 343" aria-hidden="true">
    <polygon points="0,22 600,22 600,205 0,182" fill="var(--green)"/>
    <rect x="0" y="22" width="380" height="16" fill="var(--orange)"/>
    <rect x="555" y="118" width="45" height="14" fill="var(--orange)"/>
    <path d="M30 98 V80 H46" fill="none" stroke="var(--rule)" stroke-width="1.5"/>
    <path d="M300 146 V160 H600" fill="none" stroke="var(--rule)" stroke-width="1.5"/>
  </svg>

  <div class="brand-name">Qorvil</div>

  <div class="holder">
    <div class="holder__name">Olena Dovbush</div>
    <div class="holder__title">Director of Marketing</div>
  </div>

  <div class="contacts">
    <div class="contact">
      <svg class="contact__icon" viewBox="0 0 50 50" aria-label="Cell phone">
        <circle cx="25" cy="25" r="22" fill="none" stroke="var(--orange)" stroke-width="2"/>
        <rect x="18" y="12" width="14" height="26" rx="2.5" fill="none" stroke="var(--orange)" stroke-width="2.2"/>
        <line x1="18" y1="16.5" x2="32" y2="16.5" stroke="var(--orange)" stroke-width="1.5"/>
        <line x1="18" y1="33" x2="32" y2="33" stroke="var(--orange)" stroke-width="1.5"/>
      </svg>
      <span class="contact__text">XXX.XXX.XXXX</span>
    </div>
    <div class="contact">
      <svg class="contact__icon" viewBox="0 0 50 50" aria-label="Email">
        <circle cx="25" cy="25" r="22" fill="none" stroke="var(--orange)" stroke-width="2"/>
        <rect x="12" y="16" width="26" height="18" fill="var(--orange)"/>
        <polyline points="12,16 25,27 38,16" fill="none" stroke="#fff" stroke-width="1.8"/>
      </svg>
      <span class="contact__text">helen.dovbush@mailvane.example</span>
    </div>
    <div class="contact">
      <svg class="contact__icon" viewBox="0 0 50 50" aria-label="Business phone">
        <circle cx="25" cy="25" r="22" fill="none" stroke="var(--orange)" stroke-width="2"/>
        <path d="M17 13 l5 -2 l4 8 l-3.5 2.5 q2 5 6.5 8 l2.5 -3.5 l8 4 l-2 5 q-3 3 -8 0 q-9 -6 -13.5 -15 q-2 -5 1 -7 z" fill="var(--orange)"/>
      </svg>
      <span class="contact__text">780.555.0187</span>
    </div>
  </div>
</section>

<section class="card card--back" aria-label="Business card back">
  <svg class="card__shapes" viewBox="0 0 600 343" aria-hidden="true">
    <rect x="0" y="176" width="600" height="167" fill="var(--green)"/>
    <rect x="0" y="104" width="105" height="13" fill="var(--orange)"/>
    <rect x="478" y="104" width="122" height="13" fill="var(--orange)"/>
  </svg>

  <div class="brand-name">Qorvil</div>

  <div class="web">
    <div class="web__url">www.qorvil.example</div>
    <div class="web__address">20917 - 87 Ave. Edmonton, AB, Canada. T6K 2R8</div>
  </div>
</section>

</body>
</html>
```